ちょっと急いでおりまして、
当方デザインをする時間がないので、
アウトソーシングしたいと思います。

文章、と構成だけを作りましたので、
宜しければ、お願い致します。

TAVELIA JAPAN で使用する、
お客さまにブランディングするための、
青嶺かやどり の パンフレットです。

PDFで、説明文を記載致しますので、
また見ておいて下さい。

画像素材も、添付させて頂きます。
「青嶺かやどり・かやたまご」を使うフォントは、
明朝体です。アウトラインしたデータも
添付いたします。それを活用下さい。

A4サイズ (裏・表)
両面カラーでで作っていただけると幸いです。

※もしかすると、A0サイズで引き伸ばしてつかうかもしれません。
どうぞよろしくお願い致します。

何か御不明な点がございましたら、お気軽に
ご質問ください。

当社青嶺かやどりの商品ページです。
参考にして下さい。
http://item.shopmarket-example.jp/poultry-hoshino/20004681/

青嶺かやどり協議会の ページです。
http://www.kayadori-example.com/
素材を添付いたします。レイヤーを使っておりますので、分解してください。
このページにある

の画像のような感じで、要約していただけると
幸いです。
画像を追加いたしました。
タイトルが、4Aに なってました。

すみません。A4ポスターです。
循環型の 111 のような 感じで、

ぐるっと 回る ように わかりやすく つくって頂けると幸いです。
かやどりの アニメーションデータは、

aiファイル イラストレーターの
かやたまご に 入っています。

レイヤーで組んでいますが、それを修正して作って下さい。
素材 画像を追加いたしました。
素材追加いたします。

111、222、333、444画像は、見本画像です。
イメージの参考になるかも?と思いまして、
かやどり からでる 副産物の 鶏糞堆肥もっこもこ の画像を 追加いたします。

裏側の、一番重要な情報を綺麗にまとめてくださりました。
そして、私達が やっていることに対して 共感頂けたことが大きかったです。
少し修正頂きたい部分がありますので、御連絡頂けると幸いです。

皆様 急な対応、ありがとうございます。
10件も御応募いただけるとは思っても居なかったのと、
そして、みなさんからの提案が本当に良かったので。
こちらとしても 悩ましかったです。
御提案くださった皆様。本当に、ありがとうございましたm(__)m

```html
<!DOCTYPE html>
<html lang="ja">
<head>
<meta charset="utf-8">
<title>青嶺かやどり パンフレット</title>
<link rel="stylesheet" href="https://fonts.googleapis.com/css2?family=Noto+Serif+JP:wght@500;700;900&family=Noto+Sans+JP:wght@400;500;700&display=swap">
<style>
:root{
  --red:#c4161c;
  --red-dark:#9e1016;
  --ink:#333;
  --paper:#ffffff;
  --blossom-a:#fbf4f4;
  --blossom-b:#f1dcdf;
  --green:#3f8a3a;
  --brown:#7a4b2a;
}
*{margin:0;padding:0;box-sizing:border-box}
html,body{width:846px;height:1200px;overflow:hidden}
body{font-family:"Noto Sans JP",sans-serif;color:var(--ink);background:var(--paper)}
.sheet{position:relative;width:846px;height:1200px;overflow:hidden}
.backdrop{position:absolute;inset:0;background:radial-gradient(circle at 30% 20%,var(--blossom-a),var(--blossom-b) 60%,#e8cfd3)}
.panel{position:absolute;background:rgba(255,255,255,.93);border-radius:6px;box-shadow:0 1px 4px rgba(0,0,0,.15)}
.panel-title{background:var(--red);color:#fff;font-family:"Noto Serif JP",serif;font-weight:900;text-align:center;line-height:1.3;border-radius:6px 6px 0 0}
.panel-body{font-size:10.5px;line-height:1.75;padding:10px 16px}
.panel-body em{font-style:normal;color:var(--red);font-weight:700}
.feed{left:16px;top:16px;width:390px;height:210px}
.feed .panel-title{font-size:22px;padding:8px 10px}
.nature{left:440px;top:16px;width:390px;height:240px}
.nature .panel-title{font-size:22px;padding:8px 10px}
.cycle{position:absolute;left:20px;top:232px;width:550px;height:470px}
.cycle svg{position:absolute;left:0;top:0;overflow:visible}
.step{position:absolute;font-size:10px;line-height:1.5;width:110px;background:rgba(255,255,255,.92);padding:4px 6px;border-radius:4px}
.step b{color:var(--red);font-size:12px;margin-right:2px}
.thumb{position:absolute;width:58px;height:58px;border-radius:50%;border:3px solid #fff;box-shadow:0 1px 3px rgba(0,0,0,.25)}
.center-note{position:absolute;left:235px;top:128px;width:80px;font-size:10px;text-align:center;line-height:1.4;font-weight:500}
.soil{left:590px;top:300px;width:240px;height:420px}
.soil-head{font-family:"Noto Serif JP",serif;font-weight:900;color:var(--brown);text-align:center;padding:12px 0 6px;line-height:1.2}
.soil-head small{display:block;font-size:17px}
.soil-head span{font-size:28px}
.soil-sub{margin:4px 14px;background:var(--green);color:#fff;font-weight:700;font-size:13px;text-align:center;padding:5px;border-radius:3px}
.soil .panel-body{font-size:10.5px;padding:8px 14px}
.soil .panel-body p{margin-bottom:4px}
.juicy{left:16px;top:712px;width:500px;height:472px}
.juicy .panel-title{font-size:26px;padding:10px}
.juicy .lead{font-family:"Noto Serif JP",serif;color:var(--red);font-weight:900;font-size:17px;line-height:1.55;padding:14px 18px 6px}
.juicy .panel-body{font-size:11px;padding:6px 18px}
.juicy .panel-body p{margin-bottom:8px}
.meat{position:absolute;left:530px;top:730px;width:300px;height:300px;border-radius:8px;background:radial-gradient(circle at 45% 45%,#e9a99a,#c66a5a 60%,#a84c40)}
</style>
</head>
<body>
<div class="sheet">
  <div class="backdrop" role="img" aria-label="白い梅の花が咲く枝の写真"></div>

  <section class="panel feed">
    <h2 class="panel-title">紀州の梅酢を飼料に<br>した贅沢な鶏</h2>
    <div class="panel-body">
      <p>和歌山と言えば、梅とみかんをイメージされる方も多いと思います。</p>
      <p>和歌山県の特産品のひとつである紀州南高梅の梅干しを作る際に出る梅酢を飼料に混ぜて育てたのが<em>「青嶺かや鶏」</em>です。梅酢の成分が鶏の健康を支え、元気に育ちます。</p>
    </div>
  </section>

  <section class="panel nature">
    <h2 class="panel-title">自然豊かな環境で<br>すくすく育ちました</h2>
    <div class="panel-body">
      <p>和歌山県の山あいに位置する農場では、きれいな空気と水に恵まれ、<em>「平飼い」</em>という鶏が自由に動ける環境で、ストレスの少ない飼育をしています。</p>
      <p>のびのびと動き回ることで筋肉がしっかりと発達し、旨味のある肉質に育ちます。日々の健康管理も丁寧に行っています。</p>
    </div>
  </section>

  <div class="cycle">
    <svg width="550" height="470" viewBox="0 0 550 470">
      <defs><path id="arcTitle" d="M55 255 A220 220 0 0 1 495 255"/></defs>
      <circle cx="275" cy="255" r="165" fill="none" stroke="#fff" stroke-width="22" opacity=".85"/>
      <circle cx="275" cy="255" r="165" fill="none" stroke="var(--red)" stroke-width="2" stroke-dasharray="6 6"/>
      <text font-family="Noto Serif JP, serif" font-weight="900" font-size="22" fill="var(--red)">
        <textPath href="#arcTitle" startOffset="50%" text-anchor="middle">地球に優しい 青嶺かやどりの取り組み</textPath>
      </text>
      <circle cx="275" cy="255" r="92" fill="#c9b6a8" stroke="#fff" stroke-width="5" role="img" aria-label="鶏を抱く生産者の写真"/>
      <polygon points="400,150 412,166 394,166" fill="var(--red)"/>
      <polygon points="150,360 138,344 156,344" fill="var(--red)"/>
    </svg>
    <div class="center-note">梅を作る人と<br>鶏を育てる人</div>

    <div class="thumb" style="left:150px;top:150px;background:#c0392b" role="img" aria-label="梅干しの写真"></div>
    <div class="step" style="left:20px;top:160px"><b>①</b>梅の農家が南高梅で梅干しを作ります</div>

    <div class="thumb" style="left:145px;top:245px;background:#d98c8c" role="img" aria-label="梅酢の写真"></div>
    <div class="step" style="left:20px;top:250px"><b>②</b>梅干しを作る際に出る梅酢を飼料に</div>

    <div class="thumb" style="left:160px;top:335px;background:#e6d7b8" role="img" aria-label="鶏の写真"></div>
    <div class="step" style="left:30px;top:345px"><b>③</b>梅酢入りの飼料で青嶺かやどりを育てます</div>

    <div class="thumb" style="left:330px;top:335px;background:#8a6a4a" role="img" aria-label="鶏ふんの写真"></div>
    <div class="step" style="left:400px;top:345px"><b>④</b>鶏ふんをじっくり発酵させ堆肥にします</div>

    <div class="thumb" style="left:345px;top:245px;background:#6b4a30" role="img" aria-label="発酵堆肥の写真"></div>
    <div class="step" style="left:415px;top:250px"><b>⑤</b>発酵鶏ふん堆肥を梅畑にまきます</div>

    <div class="thumb" style="left:340px;top:150px;background:#7fa35a" role="img" aria-label="梅の木の写真"></div>
    <div class="step" style="left:410px;top:160px"><b>⑥</b>堆肥で梅の木が元気に育ち実をつけます</div>
  </div>

  <section class="panel soil">
    <h2 class="soil-head"><small>いのちの土</small><span>もっこもこ</span></h2>
    <p class="soil-sub">環境に優しい<br>発酵鶏ふん堆肥</p>
    <div class="panel-body">
      <p>①紀州の梅酢で育った鶏のフンに</p>
      <p>②梅干しを作った後の調整液を混ぜ合わせ</p>
      <p>③ゆっくりじっくり発酵させた堆肥です</p>
      <p>④植物や作物がすくすく元気に育ってくれます</p>
      <p>自然の恵みが詰まった「いのちの土 もっこもこ」で、梅の木も野菜もふかふかの土で元気に育ちます。</p>
    </div>
  </section>

  <section class="panel juicy">
    <h2 class="panel-title">保水性に優れた<br>ジューシーチキン</h2>
    <p class="lead">鶏の赤い筋肉を発達させることで水分が抜け落ちにくい鶏肉に。肉の水分を逃がさないから、かやどりはパサつかず旨味たっぷり！</p>
    <div class="panel-body">
      <p>青嶺かやどりの鶏肉は保水性に優れていることが、保水性の高さの研究でも確かめられています。</p>
      <p>従来の鶏肉は「脂がのるように」と太らせて育てるのですが、青嶺かやどりは、比較的小さな体で運動量が多く、赤い筋肉が発達しています。</p>
      <p>一方、鶏肉を配合する際や冷凍して解凍する際でも、ドリップが出にくく、肉のうま味をしっかり閉じ込めます。そのため、焼いても煮ても、ふっくらジューシーな仕上がりになります。</p>
    </div>
  </section>

  <div class="meat" role="img" aria-label="ジューシーな鶏肉の写真"></div>
</div>
</body>
</html>
```